Gestaltung Deutschlandfahne
Zielgruppe
Quendal Verkäufer / Quendal Käufer
Aufgabenstellung
Gestaltung einer Deutschlandfahne.
Frei in der Gestaltung nach vorgegebener Skizze

```html
<!DOCTYPE html>
<html lang="de">
<head>
<meta charset="utf-8">
<title>Deutschlandfahne – Entwürfe</title>
<link rel="stylesheet" href="https://fonts.googleapis.com/css2?family=Montserrat:wght@800&display=swap">
<style>
  :root {
    --flag-black: #050508;
    --flag-red: #e21e1f;
    --flag-gold: #f6c91b;
    --star-gold: #f7b81a;
    --star-light: #fde047;
    --white: #ffffff;
    --page: #ffffff;
  }
  * { margin: 0; padding: 0; box-sizing: border-box; }
  html, body {
    width: 1200px;
    height: 765px;
    overflow: hidden;
    background: var(--page);
  }
  .sheet {
    position: relative;
    width: 1200px;
    height: 765px;
  }
  .flag {
    position: absolute;
    top: 206px;
    width: 590px;
    height: 352px;
    overflow: hidden;
    display: flex;
    flex-direction: column;
  }
  .flag--map { left: 0; }
  .flag--year { left: 611px; }
  .stripe { flex: 1; }
  .stripe--black { background: var(--flag-black); }
  .stripe--red { background: var(--flag-red); }
  .stripe--gold { background: var(--flag-gold); }

  .map-area {
    position: absolute;
    left: 140px;
    top: 9px;
    width: 312px;
    height: 335px;
    border-radius: 38% 42% 30% 34% / 30% 34% 40% 44%;
    background: radial-gradient(ellipse at 50% 50%, rgba(255,255,255,0.42), rgba(255,255,255,0.18) 70%, rgba(255,255,255,0.05));
  }

  .stars {
    position: absolute;
    left: 172px;
    top: 33px;
    width: 245px;
    height: 48px;
  }

  .ball-area {
    position: absolute;
    left: 191px;
    top: 102px;
    width: 212px;
    height: 226px;
    border-radius: 50%;
    background: radial-gradient(circle at 50% 45%, rgba(255,255,255,0.85), rgba(255,255,255,0.45) 60%, rgba(255,255,255,0.15));
  }

  .year {
    position: absolute;
    font-family: "Montserrat", sans-serif;
    font-weight: 800;
    color: var(--white);
    line-height: 1;
    letter-spacing: -2px;
    text-shadow: 3px 5px 6px rgba(0,0,0,0.35);
    transform: rotate(-5deg);
    transform-origin: left bottom;
  }
  .year--start {
    left: 26px;
    top: 178px;
    font-size: 112px;
  }
  .year--end {
    left: 412px;
    top: 130px;
    font-size: 108px;
  }
</style>
</head>
<body>
<main class="sheet">

  <section class="flag flag--map" aria-label="Fahne mit Deutschlandkarte">
    <div class="stripe stripe--black"></div>
    <div class="stripe stripe--red"></div>
    <div class="stripe stripe--gold"></div>
    <div class="map-area" role="img" aria-label="Gepunktete Deutschlandkarte mit Fußbällen an den Spielorten"></div>
  </section>

  <section class="flag flag--year" aria-label="Fahne mit Fußball und Jahreszahl">
    <div class="stripe stripe--black"></div>
    <div class="stripe stripe--red"></div>
    <div class="stripe stripe--gold"></div>

    <svg class="stars" viewBox="0 0 245 48" aria-hidden="true">
      <defs>
        <polygon id="star" points="24,0 29.6,17.3 47.7,17.3 33.1,28 38.7,45.3 24,34.6 9.3,45.3 14.9,28 0.3,17.3 18.4,17.3"/>
      </defs>
      <g fill="var(--star-gold)">
        <use href="#star" x="0"/>
        <use href="#star" x="65"/>
        <use href="#star" x="130"/>
        <use href="#star" x="195"/>
      </g>
      <g fill="var(--star-light)" opacity="0.7">
        <polygon points="24,0 24,34.6 9.3,45.3 14.9,28 0.3,17.3 18.4,17.3"/>
        <polygon transform="translate(65 0)" points="24,0 24,34.6 9.3,45.3 14.9,28 0.3,17.3 18.4,17.3"/>
        <polygon transform="translate(130 0)" points="24,0 24,34.6 9.3,45.3 14.9,28 0.3,17.3 18.4,17.3"/>
        <polygon transform="translate(195 0)" points="24,0 24,34.6 9.3,45.3 14.9,28 0.3,17.3 18.4,17.3"/>
      </g>
    </svg>

    <div class="ball-area" role="img" aria-label="Illustrierter Fußball im Grunge-Stil in den Fahnenfarben"></div>

    <span class="year year--start">20</span>
    <span class="year year--end">24</span>
  </section>

</main>
</body>
</html>
```